Tidal Homecare

I am looking to have a website designed for a housekeeping company that looks similar to this one. https://marlowestidyhomes.example/

I need 5 websites designed but will start with this one to see how I like it.

Industry/Entity Type

House Cleaning

Coding

Coded - Design and coding required

Number of Pages Required

5+ page

Font styles to use
Serif
Script

Colors
ffffff
fdf9cf
fbf289
fbee3f
d6edf3
86cae7
33a6d7
edf1f8
cedeed

```html
<!DOCTYPE html>
<html lang="en">
<head>
<meta charset="utf-8">
<title>Tidal Homecare – Pricing</title>
<link href="https://fonts.googleapis.com/css2?family=Oswald:wght@400;500&family=Poppins:wght@400;500;600&display=swap" rel="stylesheet">
<style>
:root{
  --blue:#0081c2;
  --blue-light:#0aa6ee;
  --ink:#262626;
  --text:#555;
  --row-a:#f7f7f7;
  --row-b:#f0f0f0;
  --footer:#282828;
  --white:#fff;
  --muted:#9a9a9a;
}
*{margin:0;padding:0;box-sizing:border-box}
html,body{width:758px;height:1200px;overflow:hidden;background:var(--white)}
body{position:relative;font-family:'Poppins',sans-serif;color:var(--text)}
.abs{position:absolute}
.header{top:0;left:0;width:758px;height:52px;background:var(--white);z-index:2}
.brand{font-family:'Oswald',sans-serif;font-weight:400;font-size:19px;line-height:20px;color:var(--ink);letter-spacing:.5px;text-transform:uppercase}
.header .brand{left:102px;top:7px;width:100px}
.nav{left:290px;top:20px;display:flex;gap:0;font-size:7px;font-weight:500;text-transform:uppercase;color:#444}
.nav a{color:inherit;text-decoration:none;margin-right:21px}
.nav a.active{color:var(--blue-light)}
.call-btn{left:552px;top:13px;width:104px;height:26px;border-radius:13px;background:linear-gradient(90deg,var(--blue),var(--blue-light));color:var(--white);font-family:'Oswald',sans-serif;font-size:11px;display:flex;align-items:center;justify-content:center;gap:5px}
.hero{top:52px;left:0}
.hero-title{top:122px;left:0;width:758px;text-align:center;font-family:'Oswald',sans-serif;font-size:38px;font-weight:400;color:var(--ink)}
.section-title{left:0;width:758px;text-align:center;font-family:'Oswald',sans-serif;font-size:28px;font-weight:400;color:var(--ink)}
.section-title span{color:var(--blue)}
.rate-table{width:272px;font-size:7px;border-collapse:collapse}
.rate-table th{height:24px;text-align:left;padding-left:7px;font-family:'Oswald',sans-serif;font-weight:400;font-size:10px;color:var(--white);background:var(--ink)}
.rate-table.homes th{background:var(--blue)}
.rate-table td{height:23.7px;padding-left:10px;color:var(--text)}
.rate-table td.price{color:var(--blue);font-weight:600;padding-left:0;width:107px}
.rate-table tr:nth-child(odd) td{background:var(--row-a)}
.rate-table tr:nth-child(even) td{background:var(--row-b)}
.contact-btn{left:336px;top:941px;width:86px;height:23px;border-radius:12px;background:linear-gradient(90deg,var(--blue),var(--blue-light));color:var(--white);font-family:'Oswald',sans-serif;font-size:10px;display:flex;align-items:center;justify-content:center}
.footer-brand{left:102px;top:1111px;width:100px;color:var(--white)}
.copyright{left:103px;top:1163px;width:120px;font-size:6.5px;line-height:10px;color:var(--muted)}
.copyright b{color:#ddd;font-weight:400}
.footer-links{left:247px;top:1107px;list-style:none;font-size:7px;line-height:16.7px;color:var(--muted)}
.footer-links li:first-child{color:var(--blue-light)}
.footer-phone{left:406px;top:1102px;font-family:'Oswald',sans-serif;font-size:12px;color:var(--white)}
.footer-email{left:402px;top:1131px;font-size:7px;color:var(--muted)}
.social{left:549px;top:1113px;display:flex;gap:7px}
.social span{width:21px;height:21px;border-radius:50%;background:var(--white)}
.social span:first-child{background:var(--blue-light)}
</style>
</head>
<body>

<header class="abs header">
  <div class="abs brand">Tidal<br>Homecare</div>
  <nav class="abs nav">
    <a href="#">Home</a><a href="#">Service</a><a href="#" class="active">Pricing</a><a href="#">About Us</a><a href="#">Contact Us</a>
  </nav>
  <div class="abs call-btn">
    <svg width="9" height="9" viewBox="0 0 24 24"><path fill="#fff" d="M6.6 10.8c1.4 2.8 3.8 5.1 6.6 6.6l2.2-2.2c.3-.3.7-.4 1-.2 1.1.4 2.3.6 3.6.6.6 0 1 .4 1 1V20c0 .6-.4 1-1 1C10.6 21 3 13.4 3 4c0-.6.4-1 1-1h3.5c.6 0 1 .4 1 1 0 1.3.2 2.5.6 3.6.1.3 0 .7-.2 1z"/></svg>
    555 014 2290
  </div>
</header>

<svg class="abs hero" width="758" height="280" viewBox="0 52 758 280">
  <defs>
    <linearGradient id="sheets" x1="0" y1="0" x2="1" y2="1">
      <stop offset="0" stop-color="#e4e5e7"/>
      <stop offset=".5" stop-color="#f4f4f5"/>
      <stop offset="1" stop-color="#e9eaeb"/>
    </linearGradient>
    <linearGradient id="waveBlue" x1="0" y1="0" x2="1" y2="0">
      <stop offset="0" stop-color="#0081c2"/>
      <stop offset="1" stop-color="#0aa6ee"/>
    </linearGradient>
  </defs>
  <rect x="0" y="52" width="758" height="280" fill="url(#sheets)" role="img" aria-label="Photo of a freshly made white bed with rumpled blanket and pillows"/>
  <path d="M0 268 C110 322 260 330 420 282 C560 240 680 205 758 285 L758 332 L0 332Z" fill="url(#waveBlue)"/>
  <path d="M0 272 C120 318 270 322 430 284 C570 250 690 225 758 292 L758 332 L0 332Z" fill="#fff"/>
  <path d="M0 272 C120 318 270 322 430 284" fill="none" stroke="none"/>
</svg>
<h1 class="abs hero-title">Pricing</h1>

<h2 class="abs section-title" style="top:360px">Cleaning Rates <span>starting at</span></h2>
<table class="abs rate-table" style="left:102px;top:425px">
  <tr><th colspan="2">Condo</th></tr>
  <tr><td>Studio</td><td class="price">$159.00</td></tr>
  <tr><td>1 Bedroom</td><td class="price">$179.00</td></tr>
  <tr><td>2 Bedroom</td><td class="price">$229.00</td></tr>
  <tr><td>3 Bedroom</td><td class="price">$259.00</td></tr>
</table>
<table class="abs rate-table homes" style="left:384px;top:425px">
  <tr><th colspan="2">Homes</th></tr>
  <tr><td>1 Bedroom House</td><td class="price">$219.00</td></tr>
  <tr><td>2 Bedroom House</td><td class="price">$259.00</td></tr>
  <tr><td>3 Bedroom</td><td class="price">$319.00</td></tr>
  <tr><td>4 bedroom +</td><td class="price">$399.00</td></tr>
</table>

<h2 class="abs section-title" style="top:592px">Deep <span>Cleaning Rates</span></h2>
<table class="abs rate-table" style="left:102px;top:643px">
  <tr><th colspan="2">Condo</th></tr>
  <tr><td>Studio</td><td class="price">$219.00</td></tr>
  <tr><td>1 Bedroom</td><td class="price">$249.00</td></tr>
  <tr><td>2 Bedroom</td><td class="price">$329.00</td></tr>
  <tr><td>3 Bedroom</td><td class="price">$449.00</td></tr>
</table>
<table class="abs rate-table homes" style="left:384px;top:643px">
  <tr><th colspan="2">Homes</th></tr>
  <tr><td>1 Bedroom House</td><td class="price">$319.00</td></tr>
  <tr><td>2 Bedroom House</td><td class="price">$499.00</td></tr>
  <tr><td>3 Bedroom</td><td class="price">$579.00</td></tr>
  <tr><td>4 bedroom +</td><td class="price">$789.00</td></tr>
</table>

<h2 class="abs section-title" style="top:810px">Other Services <span>Starting at</span></h2>
<table class="abs rate-table" style="left:243px;top:862px">
  <tr><td>Pressure Washing</td><td class="price">$1.75/Foot</td></tr>
  <tr><td>Window Washing</td><td class="price">$10/Window</td></tr>
</table>

<div class="abs contact-btn">CONTACT US</div>

<svg class="abs" style="top:1000px;left:0" width="758" height="200" viewBox="0 1000 758 200">
  <path d="M0 1030 C120 1100 280 1090 420 1052 C560 1012 700 985 758 1045 L758 1200 L0 1200Z" fill="#282828"/>
</svg>

<div class="abs brand footer-brand">Tidal<br>Homecare</div>
<p class="abs copyright">© <b>Tidal Homecare</b> - 2020. All Right Reserved.</p>
<ul class="abs footer-links">
  <li>Home</li><li>Service Offered</li><li>About Us</li><li>Contact Us</li>
</ul>
<svg class="abs" style="left:389px;top:1110px" width="12" height="12" viewBox="0 0 24 24"><path fill="#fff" d="M6.6 10.8c1.4 2.8 3.8 5.1 6.6 6.6l2.2-2.2c.3-.3.7-.4 1-.2 1.1.4 2.3.6 3.6.6.6 0 1 .4 1 1V20c0 .6-.4 1-1 1C10.6 21 3 13.4 3 4c0-.6.4-1 1-1h3.5c.6 0 1 .4 1 1 0 1.3.2 2.5.6 3.6.1.3 0 .7-.2 1z"/></svg>
<div class="abs footer-phone">555 014 2290</div>
<svg class="abs" style="left:389px;top:1137px" width="10" height="8" viewBox="0 0 10 8"><rect x=".5" y=".5" width="9" height="7" fill="none" stroke="#9a9a9a"/><path d="M.5 .8 5 4.5 9.5 .8" fill="none" stroke="#9a9a9a"/></svg>
<div class="abs footer-email">hello@tidalhomecare.example</div>
<div class="abs social"><span></span><span></span><span></span><span></span></div>

</body>
</html>
```